Real Estate Webpage Design

We have an existing website: brindlewoodhomes.com.au
We focus customised service mainly on Property Management and second-hand property sales.
We are not entirely happy about the current design and layout can stay roughly the same as the back end coding is linked to a CRM system.
We would like to see the design are more reachable to our clients and appearing.
Please check our Website Design Draft for more details.

Industry/Entity Type

Real estate Agency

Number of Pages Required

5+ page

Font styles to use
Sans Serif

Colors

Designer to choose colors to be used in the design.

```html
<!DOCTYPE html>
<html lang="en">
<head>
<meta charset="utf-8">
<title>Brindlewood Property Group</title>
<link href="https://fonts.googleapis.com/css2?family=Poppins:wght@400;500;600;700&display=swap" rel="stylesheet">
<style>
:root{
  --orange:#f6a91b;
  --navy:#1f2533;
  --ink:#22252c;
  --muted:#7a7f89;
  --line:#e4e6ea;
  --soft:#f6f7f9;
  --white:#ffffff;
}
*{box-sizing:border-box;margin:0;padding:0}
html,body{width:1200px;height:3180px;overflow:hidden}
body{font-family:"Poppins",sans-serif;color:var(--ink);background:var(--white);position:relative}
.abs{position:absolute}
a{color:inherit;text-decoration:none}

/* header */
.brand{left:112px;top:28px;display:flex;align-items:center;gap:12px}
.brand-mark{width:34px;height:34px;background:var(--orange)}
.brand-name{font-size:26px;font-weight:600;color:var(--ink);line-height:1}
.nav{left:400px;top:38px;display:flex;gap:52px;font-size:15px;font-weight:500}
.nav .active{border-bottom:3px solid var(--orange);padding-bottom:6px}
.btn{display:inline-block;border-radius:22px;font-size:14px;font-weight:600;padding:11px 24px}
.btn-orange{background:var(--orange);color:var(--ink)}
.btn-dark{background:var(--navy);color:var(--white)}
.nav-cta{left:1000px;top:28px}

/* hero */
.hero-title{left:100px;top:216px;font-size:48px;font-weight:700;line-height:1}
.hero-sub{left:128px;top:278px;font-size:22px;font-weight:600}
.hero-sub span{font-size:38px;font-weight:600}
.hero-copy{left:100px;top:340px;width:470px;font-size:13px;line-height:1.75;color:var(--muted)}
.hero-copy p+p{margin-top:14px}
.hero-actions{left:100px;top:500px;display:flex;gap:18px}
.hero-block-dark{left:590px;top:80px;width:90px;height:90px;background:var(--navy)}
.hero-block-orange{left:980px;top:430px;width:160px;height:140px;background:var(--orange)}
.hero-photo{left:620px;top:84px;width:480px;height:460px;border-radius:4px;background:linear-gradient(160deg,#cfd7dc 0%,#9aa6a9 45%,#7d715f 75%,#5f6b4e 100%)}

/* intro */
.section-icon{width:22px;height:22px;border:4px solid var(--orange);border-right:none;border-bottom:none}
.intro-icon{left:589px;top:620px}
.intro-title{left:0;top:652px;width:1200px;text-align:center;font-size:34px;font-weight:600;line-height:1.3}
.rule{left:100px;width:1000px;height:1px;background:var(--line)}

/* listings */
.listings-bg{left:0;top:830px;width:1200px;height:660px;background:var(--soft)}
.listings-icon{left:78px;top:864px}
.listings-title{left:100px;top:870px;font-size:34px;font-weight:600;line-height:1.25}
.tabs{left:620px;top:904px;display:flex;gap:10px}
.tab{font-size:13px;font-weight:500;padding:9px 22px;border-radius:20px;background:var(--white)}
.tab.active{background:var(--navy);color:var(--white)}
.cards{left:100px;top:1000px;display:flex;gap:20px}
.card{width:235px;height:380px;background:var(--white);border-radius:6px;box-shadow:0 6px 18px rgba(0,0,0,.07);padding:14px;display:flex;flex-direction:column}
.card-photo{height:160px;border-radius:4px;flex:none}
.card-suburb{font-size:10px;color:var(--muted);margin-top:12px;text-transform:uppercase;letter-spacing:.5px}
.card-address{font-size:13px;font-weight:600;margin-top:2px;line-height:1.4}
.card-feats{display:flex;gap:14px;margin-top:8px;font-size:12px;color:var(--muted);align-items:center}
.card-feats svg{width:14px;height:14px;vertical-align:-2px;margin-right:4px}
.card-price{font-size:14px;font-weight:600;margin-top:8px}
.card-inspect{font-size:10px;color:var(--muted);margin-top:4px;line-height:1.5}
.card-foot{display:flex;gap:12px;margin-top:auto}
.card-foot svg{width:16px;height:16px}
.view-all{left:545px;top:1412px}

/* testimonials */
.room-photo{left:0;top:1580px;width:490px;height:460px;background:linear-gradient(120deg,#ffffff 0%,#f0ede8 40%,#e2d8cb 75%,#ffffff 100%)}
.reviews-icon{left:382px;top:1528px}
.reviews-title{left:410px;top:1534px;font-size:34px;font-weight:600}
.arrows{left:1020px;top:1548px;display:flex;gap:10px}
.arrow{width:36px;height:36px;border-radius:50%;background:var(--white);box-shadow:0 3px 10px rgba(0,0,0,.12);display:flex;align-items:center;justify-content:center}
.review{width:310px;height:220px;background:var(--white);box-shadow:0 8px 22px rgba(0,0,0,.09);padding:24px;top:1620px}
.review-1{left:460px}
.review-2{left:800px}
.stars{color:var(--orange);font-size:14px;letter-spacing:3px}
.review p{font-size:12px;line-height:1.7;color:var(--muted);margin-top:10px}
.review .who{font-size:12px;font-weight:600;color:var(--ink);margin-top:24px}
.future-title{left:600px;top:1950px;width:380px;text-align:center;font-size:34px;font-weight:600;line-height:1.25}

/* work with us */
.work-icon{left:150px;top:2168px}
.work-title{left:0;top:2178px;width:1200px;text-align:center;font-size:34px;font-weight:600}
.work-copy{left:300px;top:2250px;width:600px;text-align:center;font-size:12px;line-height:1.7;color:var(--muted)}
.work-cta{left:540px;top:2310px}

/* map */
.map{left:60px;top:2410px;width:1080px;height:320px;background:linear-gradient(135deg,#e9ecef 0%,#dfe7dc 45%,#cfe0ec 100%)}
.map-pin{left:588px;top:2530px}

/* footer */
.corner-orange{left:0;top:2760px;width:100px;height:60px;background:var(--orange);clip-path:polygon(0 100%,60% 0,100% 0,40% 100%)}
.corner-dark{left:1100px;top:2760px;width:100px;height:60px;background:var(--navy);clip-path:polygon(40% 100%,100% 0,100% 100%)}
.footer{left:0;top:2820px;width:1200px;height:360px;background:var(--navy);color:#c5c9d1}
.foot-cols{position:absolute;left:100px;top:48px;display:flex;gap:0}
.foot-col{width:250px;font-size:12px;line-height:2}
.foot-col h4{font-size:12px;font-weight:600;color:var(--white);text-transform:uppercase;letter-spacing:.5px;margin-bottom:8px}
.foot-bar{position:absolute;left:100px;right:100px;top:300px;border-top:1px solid #343b4a;padding-top:18px;display:flex;justify-content:space-between;font-size:11px}
.foot-bar .links{display:flex;gap:28px}
</style>
</head>
<body>

<header>
  <div class="abs brand"><span class="brand-mark"></span><span class="brand-name">Brindlewood</span></div>
  <nav class="abs nav">
    <a class="active" href="#">Home</a><a href="#">About Us</a><a href="#">Leasing</a><a href="#">Buy</a><a href="#">Sell</a><a href="#">Our Team</a><a href="#">Blog</a>
  </nav>
  <a class="abs btn btn-dark nav-cta" href="#">Contact Us</a>
</header>

<section class="hero">
  <div class="abs hero-block-dark"></div>
  <div class="abs hero-block-orange"></div>
  <div class="abs hero-photo" role="img" aria-label="Photo of a modern single-storey brick home with a green front lawn"></div>
  <h1 class="abs hero-title">Brindlewood</h1>
  <div class="abs hero-sub">Built around <span>“the home”</span></div>
  <div class="abs hero-copy">
    <p>At Brindlewood Property Group we believe every home has a story, and our role is to help you write the next chapter with care, honesty and clear advice from start to finish.</p>
    <p>Bringing together local experience and a personal approach, our team manages and sells homes across the region, making sure owners and tenants feel supported, informed and confident every step of the way.</p>
  </div>
  <div class="abs hero-actions"><a class="btn btn-dark" href="#">Learn more</a><a class="btn btn-orange" href="#">Contact Us</a></div>
</section>

<section class="intro">
  <div class="abs section-icon intro-icon"></div>
  <h2 class="abs intro-title">Your Local Real Estate<br>Property Group</h2>
  <div class="abs rule" style="top:790px"></div>
</section>

<section class="listings">
  <div class="abs listings-bg"></div>
  <div class="abs section-icon listings-icon"></div>
  <h2 class="abs listings-title">This month at Brindlewood<br>Property Group</h2>
  <div class="abs tabs">
    <span class="tab">For Sale</span><span class="tab active">For Lease</span><span class="tab">Open Homes</span><span class="tab">Sold</span><span class="tab">Leased</span>
  </div>
  <div class="abs cards">
    <article class="card">
      <div class="card-photo" role="img" aria-label="Photo of a bright empty living room with timber floors" style="background:linear-gradient(160deg,#eceae6,#b9b3aa)"></div>
      <div class="card-suburb">Lawson</div>
      <div class="card-address">12 Harrowdale Terrace Lawson</div>
      <div class="card-feats">
        <span><svg viewBox="0 0 16 16"><rect x="1" y="7" width="14" height="5" fill="none" stroke="#7a7f89" stroke-width="1.5"/><path d="M1 12v2M15 12v2M3 7V4h4v3" fill="none" stroke="#7a7f89" stroke-width="1.5"/></svg>3</span>
        <span><svg viewBox="0 0 16 16"><path d="M2 8h12v2a4 4 0 0 1-4 4H6a4 4 0 0 1-4-4z" fill="none" stroke="#7a7f89" stroke-width="1.5"/></svg>2</span>
        <span><svg viewBox="0 0 16 16"><rect x="2" y="6" width="12" height="6" rx="2" fill="none" stroke="#7a7f89" stroke-width="1.5"/></svg>1</span>
      </div>
      <div class="card-price">$560 – $620 pw</div>
      <div class="card-inspect">Open for inspection<br>Sat 14 Sep 10:00 – 10:20 am</div>
      <div class="card-foot"><svg viewBox="0 0 16 16"><path d="M8 14S2 10 2 6a3 3 0 0 1 6-1 3 3 0 0 1 6 1c0 4-6 8-6 8z" fill="none" stroke="#f6a91b" stroke-width="1.5"/></svg><svg viewBox="0 0 16 16"><path d="M8 1l2 5h5l-4 3 2 5-5-3-5 3 2-5-4-3h5z" fill="#f6a91b"/></svg></div>
    </article>
    <article class="card">
      <div class="card-photo" role="img" aria-label="Photo of a two-storey grey home with garage at dusk" style="background:linear-gradient(160deg,#5d6f86,#2e3643)"></div>
      <div class="card-suburb">Bonner</div>
      <div class="card-address">8 Pemberley Street Bonner</div>
      <div class="card-feats">
        <span><svg viewBox="0 0 16 16"><rect x="1" y="7" width="14" height="5" fill="none" stroke="#7a7f89" stroke-width="1.5"/><path d="M1 12v2M15 12v2M3 7V4h4v3" fill="none" stroke="#7a7f89" stroke-width="1.5"/></svg>4</span>
        <span><svg viewBox="0 0 16 16"><path d="M2 8h12v2a4 4 0 0 1-4 4H6a4 4 0 0 1-4-4z" fill="none" stroke="#7a7f89" stroke-width="1.5"/></svg>2</span>
        <span><svg viewBox="0 0 16 16"><rect x="2" y="6" width="12" height="6" rx="2" fill="none" stroke="#7a7f89" stroke-width="1.5"/></svg>2</span>
      </div>
      <div class="card-price">$720 pw</div>
      <div class="card-inspect">Open for inspection<br>Sat 14 Sep 11:00 – 11:20 am</div>
      <div class="card-foot"><svg viewBox="0 0 16 16"><path d="M8 14S2 10 2 6a3 3 0 0 1 6-1 3 3 0 0 1 6 1c0 4-6 8-6 8z" fill="none" stroke="#f6a91b" stroke-width="1.5"/></svg><svg viewBox="0 0 16 16"><path d="M8 1l2 5h5l-4 3 2 5-5-3-5 3 2-5-4-3h5z" fill="#f6a91b"/></svg></div>
    </article>
    <article class="card">
      <div class="card-photo" role="img" aria-label="Photo of a dark modern home frontage with timber gate" style="background:linear-gradient(160deg,#8a7f72,#3b3733)"></div>
      <div class="card-suburb">Braddon</div>
      <div class="card-address">5/22 Keswick Street Braddon</div>
      <div class="card-feats">
        <span><svg viewBox="0 0 16 16"><rect x="1" y="7" width="14" height="5" fill="none" stroke="#7a7f89" stroke-width="1.5"/><path d="M1 12v2M15 12v2M3 7V4h4v3" fill="none" stroke="#7a7f89" stroke-width="1.5"/></svg>2</span>
        <span><svg viewBox="0 0 16 16"><path d="M2 8h12v2a4 4 0 0 1-4 4H6a4 4 0 0 1-4-4z" fill="none" stroke="#7a7f89" stroke-width="1.5"/></svg>1</span>
        <span><svg viewBox="0 0 16 16"><rect x="2" y="6" width="12" height="6" rx="2" fill="none" stroke="#7a7f89" stroke-width="1.5"/></svg>1</span>
      </div>
      <div class="card-price">$540 pw</div>
      <div class="card-inspect">Open for inspection<br>Sat 14 Sep 12:00 – 12:20 pm</div>
      <div class="card-foot"><svg viewBox="0 0 16 16"><path d="M8 14S2 10 2 6a3 3 0 0 1 6-1 3 3 0 0 1 6 1c0 4-6 8-6 8z" fill="none" stroke="#f6a91b" stroke-width="1.5"/></svg><svg viewBox="0 0 16 16"><path d="M8 1l2 5h5l-4 3 2 5-5-3-5 3 2-5-4-3h5z" fill="#f6a91b"/></svg></div>
    </article>
    <article class="card">
      <div class="card-photo" role="img" aria-label="Photo of a single-storey brick home under blue sky" style="background:linear-gradient(180deg,#7fa9d6 0%,#a9c3de 45%,#8a6f58 100%)"></div>
      <div class="card-suburb">Griffith</div>
      <div class="card-address">7 Larchmont Street Griffith</div>
      <div class="card-feats">
        <span><svg viewBox="0 0 16 16"><rect x="1" y="7" width="14" height="5" fill="none" stroke="#7a7f89" stroke-width="1.5"/><path d="M1 12v2M15 12v2M3 7V4h4v3" fill="none" stroke="#7a7f89" stroke-width="1.5"/></svg>3</span>
        <span><svg viewBox="0 0 16 16"><path d="M2 8h12v2a4 4 0 0 1-4 4H6a4 4 0 0 1-4-4z" fill="none" stroke="#7a7f89" stroke-width="1.5"/></svg>1</span>
        <span><svg viewBox="0 0 16 16"><rect x="2" y="6" width="12" height="6" rx="2" fill="none" stroke="#7a7f89" stroke-width="1.5"/></svg>2</span>
      </div>
      <div class="card-price">$610 pw</div>
      <div class="card-inspect">Open for inspection<br>Sat 14 Sep 1:00 – 1:20 pm</div>
      <div class="card-foot"><svg viewBox="0 0 16 16"><path d="M8 14S2 10 2 6a3 3 0 0 1 6-1 3 3 0 0 1 6 1c0 4-6 8-6 8z" fill="none" stroke="#f6a91b" stroke-width="1.5"/></svg><svg viewBox="0 0 16 16"><path d="M8 1l2 5h5l-4 3 2 5-5-3-5 3 2-5-4-3h5z" fill="#f6a91b"/></svg></div>
    </article>
  </div>
  <a class="abs btn btn-orange view-all" href="#">View All</a>
</section>

<section class="reviews">
  <div class="abs room-photo" role="img" aria-label="Soft photo of a bright dining room with table and chairs"></div>
  <div class="abs section-icon reviews-icon"></div>
  <h2 class="abs reviews-title">What they Say</h2>
  <div class="abs arrows">
    <span class="arrow"><svg width="12" height="12" viewBox="0 0 12 12"><path d="M8 2L4 6l4 4" fill="none" stroke="#22252c" stroke-width="2"/></svg></span>
    <span class="arrow"><svg width="12" height="12" viewBox="0 0 12 12"><path d="M4 2l4 4-4 4" fill="none" stroke="#22252c" stroke-width="2"/></svg></span>
  </div>
  <div class="abs review review-1">
    <div class="stars">★★★★★</div>
    <p>The team looked after our rental from day one. Every question was answered quickly and the whole process felt easy, friendly and well organised.</p>
    <div class="who">Jo Tanner</div>
  </div>
  <div class="abs review review-2">
    <div class="stars">★★★★★</div>
    <p>Very professional and caring. They explained every step of selling our home, kept us updated and achieved a result we were truly happy with.</p>
    <div class="who">Mara L</div>
  </div>
  <h2 class="abs future-title">Lead you to your<br>future home</h2>
  <div class="abs rule" style="top:2120px"></div>
</section>

<section class="work">
  <div class="abs section-icon work-icon"></div>
  <h2 class="abs work-title">Work with us and see the potential</h2>
  <p class="abs work-copy">We are here to guide you from your first enquiry to the final key handover, with honest advice and a team that treats your property like our own.</p>
  <a class="abs btn btn-orange work-cta" href="#">Contact Us</a>
</section>

<div class="abs map" role="img" aria-label="Street map showing the office location"></div>
<svg class="abs map-pin" width="24" height="34" viewBox="0 0 24 34"><path d="M12 33C12 33 2 19 2 12a10 10 0 0 1 20 0c0 7-10 21-10 21z" fill="#e5412d"/><circle cx="12" cy="12" r="4" fill="#fff"/></svg>

<div class="abs corner-orange"></div>
<div class="abs corner-dark"></div>
<footer class="abs footer">
  <div class="foot-cols">
    <div class="foot-col"><h4>Navigation</h4>Home<br>About Us<br>Buy<br>Sell<br>Our Team<br>Blog</div>
    <div class="foot-col"><h4>Leasing</h4>Properties For Lease<br>Recently Leased<br>Guide To Renting<br>Tenant Forms<br>Application Form<br>Maintenance Request<br>Lease Property</div>
    <div class="foot-col"><h4>Sell</h4>Sales Appraisal<br>Selling Tips<br>Recent Sales</div>
    <div class="foot-col"><h4>Contact</h4>Suite 4, 18 Marlow Street,<br>Dunhill ACT 2601<br>T: 02 5550 0142<br>E: hello@brindlewoodhomes.com.au<br>Mon – Fri: 9am – 5pm</div>
  </div>
  <div class="foot-bar">
    <div class="links"><span>Contact Us</span><span>Privacy</span><span>Complaints Handling</span><span>Terms of Use</span></div>
    <div>© 2024, Brindlewood Property Group. All Rights Reserved</div>
  </div>
</footer>

</body>
</html>
```